Business card design needed - Halvey Group

Halvey Group are qualified, licensed builders who provide quality, value for money solutions for anyone looking to renovate, add or extend as well as those looking to build a new home.

Read more: http://www.renovista-listings.com.au/connect/halvey/service/582031#ixzz7kWpR4m2q

Hi All, Website will NOT let me load any files so please email me for our logo.

Cheers

Industry/Entity Type

Business

Contact Information for Business Card

Halvey Group Pty. Ltd.
Marcus Halvey
0412 587 264
ACT Licensed Builders #2094371
ABN 52 781 406 239
Marcus@halvey-build.com.au

Requirements
Must have
• Name
Mobile
Email
Builders License #
ABN
Company Logo as card background (See Attached)
Matched Black reverse side of card
Should not have
• Any other images or graphic aside from logo background

```html
<!DOCTYPE html>
<html lang="en">
<head>
<meta charset="utf-8">
<title>Halvey Group – Business Card</title>
<link href="https://fonts.googleapis.com/css2?family=Inter:wght@200;300;700&display=swap" rel="stylesheet">
<style>
  :root {
    --stage: #e9e7e3;
    --silver-light: #f4f4f5;
    --silver-mid: #d4d5d8;
    --silver-dark: #b3b4b8;
    --ink: #1c1c1e;
    --ink-soft: #3a3a3d;
    --card-black: #050506;
    --mark-grey: #b9b9be;
    --mark-violet: #4b3f9e;
  }
  * { margin: 0; padding: 0; box-sizing: border-box; }
  html, body {
    width: 1200px;
    height: 804px;
    overflow: hidden;
    background: var(--stage);
    font-family: "Inter", Arial, sans-serif;
  }
  .canvas {
    position: relative;
    width: 1200px;
    height: 804px;
    display: flex;
    align-items: center;
    justify-content: center;
    gap: 40px;
  }
  .card {
    position: relative;
    width: 540px;
    height: 328px;
    border-radius: 4px;
    box-shadow: 0 2px 6px rgba(0, 0, 0, 0.18);
    overflow: hidden;
  }
  .card-front {
    background: radial-gradient(ellipse at 48% 42%, var(--silver-light) 0%, var(--silver-mid) 55%, var(--silver-dark) 100%);
    color: var(--ink);
  }
  .company-name {
    position: absolute;
    left: 26px;
    top: 26px;
    font-weight: 200;
    font-size: 43px;
    letter-spacing: -0.5px;
    color: var(--ink-soft);
    white-space: nowrap;
  }
  .person-name {
    position: absolute;
    left: 0;
    right: 0;
    top: 118px;
    text-align: center;
    font-weight: 700;
    font-size: 19px;
  }
  .credentials {
    position: absolute;
    right: 26px;
    top: 168px;
    text-align: right;
    font-weight: 300;
    font-size: 14px;
    line-height: 1.35;
    color: var(--ink-soft);
  }
  .contact {
    position: absolute;
    left: 26px;
    bottom: 26px;
    font-weight: 300;
    font-size: 14px;
    line-height: 1.35;
    color: var(--ink-soft);
  }
  .card-back {
    background: var(--card-black);
    display: flex;
    align-items: center;
    justify-content: center;
    gap: 14px;
  }
  .brand-square {
    width: 22px;
    height: 22px;
    background: var(--mark-violet);
  }
  .brand-name {
    font-weight: 700;
    font-size: 34px;
    letter-spacing: 1px;
    text-transform: uppercase;
    color: var(--mark-grey);
  }
</style>
</head>
<body>
  <main class="canvas">
    <section class="card card-front" aria-label="Business card front">
      <h1 class="company-name">Halvey Group Pty. Ltd.</h1>
      <p class="person-name">Marcus Halvey</p>
      <p class="credentials">ACT Licensed Builders #2094371<br>ABN 52 781 406 239</p>
      <p class="contact">Tel: 0412 587 264<br>marcus@halvey-build.com.au</p>
    </section>
    <section class="card card-back" aria-label="Business card back">
      <span class="brand-square"></span>
      <span class="brand-name">Halvey Group</span>
    </section>
  </main>
</body>
</html>
```